Forensic Document Examiner, looking for contemporary update to my stationery design.

Looking for professional, classy logo design for stationery and business cards. My current stationery and business card is attached.I believe a logo image makes a header section interesting, so an intriguing design of a pen, feathered pen, microscope, magnifying glass, etc., would be appropriate. I have been in the business for over 30 years. I leave ideas to the imagination of the designer.My work involves mainly, the comparison of signatures and handwriting. I also resolve alterations, obliterations, and work as shown on my website: www.documentexaminer.infoThe image produced will be printed on quality white stationery and envelopes. The stationery will be photocopied by my clients, so the images should be reproducible. The business cards may be designed in other than white.

Target Market(s)

Attorneys

Font styles to use
Sans Serif

Colors

Designer to choose colors to be used in the design.

Requirements
Must have
• Image suitable for white stationery and photocopying.
• Classy logo and image; no casual fonts.
Nice to have
• Intriguing, contemporary design incorporating a relevant logo to my work.

```html
<!DOCTYPE html>
<html lang="en">
<head>
<meta charset="utf-8">
<title>Daniel R. Hollis – Business Cards</title>
<link rel="stylesheet" href="https://fonts.googleapis.com/css2?family=Open+Sans:wght@400;600;700&family=Oswald:wght@300&display=swap">
<style>
  :root {
    --navy: #0d4a7c;
    --green: #3f9b3a;
    --ink: #1e1e1e;
    --rule: #9aa3ab;
    --paper: #f3f3f3;
    --backdrop: #5a5a5a;
  }
  * { box-sizing: border-box; margin: 0; padding: 0; }
  html, body { width: 1200px; height: 1021px; overflow: hidden; }
  body {
    background: var(--backdrop);
    font-family: "Open Sans", sans-serif;
    position: relative;
  }
  .card {
    position: absolute;
    left: 250px;
    width: 700px;
    height: 400px;
    overflow: hidden;
    box-shadow: 0 10px 30px rgba(0,0,0,.35);
  }
  .card--front { top: 70px; background: var(--navy); color: #fff; }
  .card--back { top: 540px; background: linear-gradient(120deg, #e6e6e6, var(--paper) 60%, #fafafa); color: var(--ink); }

  .lockup { position: absolute; display: flex; align-items: center; gap: 22px; }
  .lockup__mark {
    width: 70px; height: 70px; border-radius: 50%;
    background: var(--green); flex: none;
  }
  .lockup__divider { width: 2px; height: 110px; background: var(--rule); flex: none; }
  .lockup__name {
    font-weight: 700; font-size: 46px; line-height: 1;
    text-transform: uppercase; letter-spacing: .5px;
  }
  .lockup__role {
    font-family: "Oswald", sans-serif; font-weight: 300;
    font-size: 20px; letter-spacing: .5px; text-transform: uppercase;
    color: var(--rule); margin-top: 10px;
  }
  .card--front .lockup { left: 110px; top: 100px; }
  .card--front .lockup__name { color: var(--green); }
  .card--front .lockup__role { color: #b9c4cf; }
  .card--back .lockup { left: 50px; top: 48px; }
  .card--back .lockup__name { color: var(--navy); }

  .services {
    position: absolute; left: 0; right: 0; top: 268px;
    text-align: center; font-size: 19px; line-height: 1.45;
  }
  .services .sep { color: var(--green); padding: 0 4px; }

  .contact { position: absolute; left: 50px; top: 210px; font-size: 19px; line-height: 1.4; }
  .contact__row { display: flex; align-items: flex-start; gap: 12px; }
  .contact__icon { width: 22px; height: 22px; flex: none; margin-top: 3px; }
  .contact__row + .contact__row { margin-top: 4px; }

  .band-navy {
    position: absolute; left: 0; bottom: 0; width: 420px; height: 14px; background: var(--navy);
  }
  .band-green {
    position: absolute; left: 420px; right: 0; bottom: 0; height: 14px; background: var(--green);
  }
</style>
</head>
<body>

<section class="card card--front" aria-label="Card front">
  <div class="lockup">
    <span class="lockup__mark"></span>
    <span class="lockup__divider"></span>
    <div>
      <div class="lockup__name">Daniel R. Hollis</div>
      <div class="lockup__role">Forensic Document Examiner</div>
    </div>
  </div>
  <p class="services">
    Full service laboratory<span class="sep">|</span>specializing in handwriting comparisons<br>
    obliterations<span class="sep">|</span>alterations<span class="sep">|</span>indented writing recovery<span class="sep">|</span>etc.
  </p>
</section>

<section class="card card--back" aria-label="Card back">
  <div class="lockup">
    <span class="lockup__mark"></span>
    <span class="lockup__divider"></span>
    <div>
      <div class="lockup__name">Daniel R. Hollis</div>
      <div class="lockup__role">Forensic Document Examiner</div>
    </div>
  </div>

  <div class="contact">
    <div class="contact__row">
      <svg class="contact__icon" viewBox="0 0 22 22" aria-hidden="true">
        <circle cx="11" cy="11" r="11" fill="var(--green)"/>
        <rect x="5" y="7" width="12" height="8" fill="none" stroke="#fff" stroke-width="1.5"/>
        <path d="M5 7l6 5 6-5" fill="none" stroke="#fff" stroke-width="1.5"/>
      </svg>
      <span>PO Box 4120<br>Millbrook, OR 97999</span>
    </div>
    <div class="contact__row">
      <svg class="contact__icon" viewBox="0 0 22 22" aria-hidden="true">
        <circle cx="11" cy="11" r="11" fill="var(--green)"/>
        <path d="M7 6c1-1 2-1 2.5 0l1 2c.3.6 0 1-.5 1.4-.4.3-.3.8 0 1.3l1.3 1.3c.5.4 1 .5 1.3 0 .4-.5.8-.8 1.4-.5l2 1c1 .5 1 1.5 0 2.5-2 2-5 .5-7.5-2S5 8 7 6z" fill="#fff"/>
      </svg>
      <span>555-014-2297</span>
    </div>
    <div class="contact__row">
      <svg class="contact__icon" viewBox="0 0 22 22" aria-hidden="true">
        <circle cx="11" cy="11" r="11" fill="var(--green)"/>
        <text x="11" y="15.5" text-anchor="middle" font-size="13" font-weight="700" fill="#fff" font-family="Open Sans, sans-serif">@</text>
      </svg>
      <span>dhollis@quillmarkreview.example</span>
    </div>
    <div class="contact__row">
      <svg class="contact__icon" viewBox="0 0 22 22" aria-hidden="true">
        <circle cx="11" cy="11" r="11" fill="var(--green)"/>
        <g fill="none" stroke="#fff" stroke-width="1.2">
          <circle cx="11" cy="11" r="6"/>
          <ellipse cx="11" cy="11" rx="2.6" ry="6"/>
          <path d="M5 11h12M6 8h10M6 14h10"/>
        </g>
      </svg>
      <span>www.quillmarkreview.example</span>
    </div>
  </div>

  <span class="band-navy"></span>
  <span class="band-green"></span>
</section>

</body>
</html>
```